International Hand & Body company needing a Hand cream tube design for the Retail market

I am wanting a modern design for a new range of 6 hand creams I will be launching in August. They need to compliment our range of wrapped soaps which you can see on www.plomvane.com.au so am wanting clean designs. I am wanting a solid colour with a hand drawn organic feel line drawing in black elegantly placed wrapping around the label. I am wanting to focus on the colour and positioning of words and fonts. I like modern clean contemporary fonts. The final design needs to appeal to the broader female market.This may lead to range expansion if designs are well received.
Updates

These designs are not hitting the brief. They are too generic and look like a supermarket brand. Our brand is more boutique and this design needs to be modern and simple. I would like more solid colours and more modern designs. Without patterns.

Target Market(s)

Female aged 20 - 70

Requirements
Must have
• a modern contemporary design that will appeal to the masses.
• Please read attached brief.
Should not have
• a black botanical illustration, in a loose and organic design to match the fragrance.

```html
<!DOCTYPE html>
<html lang="en">
<head>
<meta charset="utf-8">
<title>plomvane hand cream labels</title>
<link rel="stylesheet" href="https://fonts.googleapis.com/css2?family=Mulish:wght@600&family=Noto+Serif:ital,wght@0,400;0,700;1,400&family=Allura&family=Roboto:wght@400;700&family=Roboto+Condensed:wght@400;700&display=swap">
<style>
  :root {
    --board: #eef2f1;
    --cream: #f8fbf1;
    --green: #5cbd3c;
    --teal: #30c994;
    --purple: #8e4fd5;
    --coral: #ff855a;
    --mauve: #93566b;
    --navy: #22347a;
  }
  * { box-sizing: border-box; margin: 0; padding: 0; }
  html, body { width: 845px; height: 1200px; overflow: hidden; }
  body { background: var(--board); position: relative; }

  .range-row { position: absolute; left: 0; width: 845px; height: 385px; display: flex; }
  .range-row.top { top: 195px; }
  .range-row.bottom { top: 620px; }

  .variant { display: flex; width: 281.66px; height: 385px; background: var(--c); }
  .panel { position: relative; width: 140.83px; height: 385px; color: var(--c); }
  .label { position: absolute; left: 14px; top: 0; width: 112px; height: 281px; background: var(--cream); }

  .brand {
    position: absolute; top: 42px; left: 0; width: 100%; text-align: center;
    font: 600 17px/1 "Mulish", sans-serif; letter-spacing: 1.6px;
  }

  .amp {
    position: absolute; left: 44px; top: 104px; width: 40px; height: 58px;
    border-radius: 50%; background: var(--c); opacity: .08;
  }
  .scent {
    position: absolute; left: 11px; top: 114px; width: 100px;
    font: 700 15px/18px "Noto Serif", serif;
  }
  .scent.split { display: flex; justify-content: space-between; left: 11px; width: 90px; }
  .scent.long { font-size: 14.5px; left: 11px; width: 100px; }

  .tagline {
    position: absolute; left: 10px; top: 200px;
    font: italic 400 8.6px/14px "Noto Serif", serif;
  }

  .script-title {
    position: absolute; top: 290px; left: 0; width: 100%; text-align: center;
    font: 400 27px/1 "Allura", cursive; color: var(--cream);
  }
  .origin {
    position: absolute; top: 347px; left: 0; width: 100%; text-align: center; color: var(--cream);
    font: 700 4.6px/1 "Roboto", sans-serif;
  }
  .volume {
    position: absolute; top: 354px; left: 0; width: 100%; text-align: center; color: var(--cream);
    font: 400 7px/1 "Roboto", sans-serif; letter-spacing: -.3px;
  }

  .claims {
    position: absolute; left: 13px; top: 92px; list-style: none;
    font: 400 8.8px/12.6px "Noto Serif", serif;
  }
  .claims li::before { content: "·"; }
  .directions {
    position: absolute; left: 14px; top: 146px; width: 92px;
    font: italic 400 6.2px/9px "Noto Serif", serif;
  }
  .ingredients {
    position: absolute; left: 14px; top: 183px; width: 86px;
    font: 400 3.9px/6.3px "Roboto Condensed", sans-serif;
  }
  .ingredients b { font-weight: 700; }
  .warnings {
    position: absolute; left: 14px; top: 249px; width: 90px;
    font: 400 3.9px/6.3px "Roboto Condensed", sans-serif;
  }

  .icon-row { position: absolute; top: 299px; left: 14px; width: 112px; height: 12px; }
  .icon { position: absolute; top: 0; width: 10px; height: 10px; border: 1.3px solid var(--cream); border-radius: 2px; }
  .icon.round { border-radius: 50%; }
  .badge { position: absolute; top: 1px; width: 9px; height: 8px; background: var(--cream); opacity: .85; border-radius: 2px; }

  .rule { position: absolute; left: 5px; width: 104px; height: 1px; background: var(--cream); }
  .rule.upper { top: 323px; }
  .rule.lower { top: 343px; }
  .skin-types {
    position: absolute; top: 331px; left: 0; width: 100%; text-align: center; color: var(--cream);
    font: 400 4.6px/1 "Roboto", sans-serif; letter-spacing: .1px;
  }
  .address {
    position: absolute; top: 349px; left: 0; width: 100%; text-align: center; color: var(--cream);
    font: 700 3.7px/1 "Roboto", sans-serif;
  }
  .contact {
    position: absolute; top: 357px; left: 0; width: 100%; text-align: center; color: var(--cream);
    font: 400 4px/1 "Roboto", sans-serif;
  }
  .contact b { font-weight: 700; }
</style>
</head>
<body>

<div class="range-row top">
  <section class="variant" style="--c: var(--green)">
    <div class="panel front">
      <div class="label">
        <p class="brand">plomvane</p>
        <div class="amp" role="img" aria-label="Faint script ampersand flourish"></div>
        <h2 class="scent split"><span>Yuzu</span><span>Sage</span></h2>
        <p class="tagline">A nourishing,<br>non-greasy<br>hand cream<br>to keep skin<br>soft &amp; hydrated</p>
      </div>
      <p class="script-title">hand cream</p>
      <p class="origin">MADE IN AUSTRALIA</p>
      <p class="volume">35 mL ℮ 1.18 fl. oz.</p>
    </div>
    <div class="panel back">
      <div class="label">
        <p class="brand">plomvane</p>
        <ul class="claims"><li>No Sulfates</li><li>No Parabens</li><li>No Mineral Oils</li><li>No Artifical Colours</li></ul>
        <p class="directions">Massage into clean dry skin<br>&nbsp;as needed</p>
        <p class="ingredients"><b>Ingredients:</b> Aqua, helianthus annuus seed (sunflower) oil, stearic acid, glycerin, cetearyl alcohol, beeswax, glyceryl stearate, dimethicone, prunus amygdalus dulcis (almond) oil, parfum, phenoxyethanol, triethanolamine, tocopheryl acetate, caprylyl glycol, theobroma cacao seed (cocoa) butter, cocos nucifera (coconut) oil, butyrospermum parki (shea) butter</p>
        <p class="warnings">Discontinue use if irritation occurs.<br>Keep away from children.<br>Avoid Contact with eyes</p>
      </div>
      <div class="icon-row">
        <span class="icon" style="left:2px"></span><span class="icon round" style="left:17px"></span>
        <span class="badge" style="left:57px"></span><span class="badge" style="left:73px"></span><span class="icon round" style="left:90px"></span>
      </div>
      <span class="rule upper" style="left:19px"></span>
      <p class="skin-types">SUITABLE FOR ALL SKIN TYPES</p>
      <span class="rule lower" style="left:19px"></span>
      <p class="address">Unit 5/12 Larkspur Road Brighton VIC 3186</p>
      <p class="contact"><b>plomvane.com.au</b> &nbsp;|&nbsp; sales@plomvane.com.au</p>
    </div>
  </section>

  <section class="variant" style="--c: var(--teal)">
    <div class="panel front">
      <div class="label">
        <p class="brand">plomvane</p>
        <div class="amp" role="img" aria-label="Faint script ampersand flourish"></div>
        <h2 class="scent split"><span>Yuzu</span><span>Sage</span></h2>
        <p class="tagline">A nourishing,<br>non-greasy<br>hand cream<br>to keep skin<br>soft &amp; hydrated</p>
      </div>
      <p class="script-title">hand cream</p>
      <p class="origin">MADE IN AUSTRALIA</p>
      <p class="volume">35 mL ℮ 1.18 fl. oz.</p>
    </div>
    <div class="panel back">
      <div class="label">
        <p class="brand">plomvane</p>
        <ul class="claims"><li>No Sulfates</li><li>No Parabens</li><li>No Mineral Oils</li><li>No Artifical Colours</li></ul>
        <p class="directions">Massage into clean dry skin<br>&nbsp;as needed</p>
        <p class="ingredients"><b>Ingredients:</b> Aqua, helianthus annuus seed (sunflower) oil, stearic acid, glycerin, cetearyl alcohol, beeswax, glyceryl stearate, dimethicone, prunus amygdalus dulcis (almond) oil, parfum, phenoxyethanol, triethanolamine, tocopheryl acetate, caprylyl glycol, theobroma cacao seed (cocoa) butter, cocos nucifera (coconut) oil, butyrospermum parki (shea) butter</p>
        <p class="warnings">Discontinue use if irritation occurs.<br>Keep away from children.<br>Avoid Contact with eyes</p>
      </div>
      <div class="icon-row">
        <span class="icon" style="left:2px"></span><span class="icon round" style="left:17px"></span>
        <span class="badge" style="left:57px"></span><span class="badge" style="left:73px"></span><span class="icon round" style="left:90px"></span>
      </div>
      <span class="rule upper" style="left:19px"></span>
      <p class="skin-types">SUITABLE FOR ALL SKIN TYPES</p>
      <span class="rule lower" style="left:19px"></span>
      <p class="address">Unit 5/12 Larkspur Road Brighton VIC 3186</p>
      <p class="contact"><b>plomvane.com.au</b> &nbsp;|&nbsp; sales@plomvane.com.au</p>
    </div>
  </section>

  <section class="variant" style="--c: var(--purple)">
    <div class="panel front">
      <div class="label">
        <p class="brand">plomvane</p>
        <div class="amp" role="img" aria-label="Faint script ampersand flourish"></div>
        <h2 class="scent">Citrus<br>Seagrass</h2>
        <p class="tagline">A nourishing,<br>non-greasy<br>hand cream<br>to keep skin<br>soft &amp; hydrated</p>
      </div>
      <p class="script-title">hand cream</p>
      <p class="origin">MADE IN AUSTRALIA</p>
      <p class="volume">35 mL ℮ 1.18 fl. oz.</p>
    </div>
    <div class="panel back">
      <div class="label">
        <p class="brand">plomvane</p>
        <ul class="claims"><li>No Sulfates</li><li>No Parabens</li><li>No Mineral Oils</li><li>No Artifical Colours</li></ul>
        <p class="directions">Massage into clean dry skin<br>&nbsp;as needed</p>
        <p class="ingredients"><b>Ingredients:</b> Aqua, helianthus annuus seed (sunflower) oil, stearic acid, glycerin, cetearyl alcohol, beeswax, glyceryl stearate, dimethicone, prunus amygdalus dulcis (almond) oil, parfum, phenoxyethanol, triethanolamine, tocopheryl acetate, caprylyl glycol, theobroma cacao seed (cocoa) butter, cocos nucifera (coconut) oil, butyrospermum parki (shea) butter</p>
        <p class="warnings">Discontinue use if irritation occurs.<br>Keep away from children.<br>Avoid Contact with eyes</p>
      </div>
      <div class="icon-row">
        <span class="icon" style="left:2px"></span><span class="icon round" style="left:17px"></span>
        <span class="badge" style="left:57px"></span><span class="badge" style="left:73px"></span><span class="icon round" style="left:90px"></span>
      </div>
      <span class="rule upper" style="left:19px"></span>
      <p class="skin-types">SUITABLE FOR ALL SKIN TYPES</p>
      <span class="rule lower" style="left:19px"></span>
      <p class="address">Unit 5/12 Larkspur Road Brighton VIC 3186</p>
      <p class="contact"><b>plomvane.com.au</b> &nbsp;|&nbsp; sales@plomvane.com.au</p>
    </div>
  </section>
</div>

<div class="range-row bottom">
  <section class="variant" style="--c: var(--coral)">
    <div class="panel front">
      <div class="label">
        <p class="brand">plomvane</p>
        <div class="amp" role="img" aria-label="Faint script ampersand flourish"></div>
        <h2 class="scent">Citrus<br>Seagrass</h2>
        <p class="tagline">A nourishing,<br>non-greasy<br>hand cream<br>to keep skin<br>soft &amp; hydrated</p>
      </div>
      <p class="script-title">hand cream</p>
      <p class="origin">MADE IN AUSTRALIA</p>
      <p class="volume">35 mL ℮ 1.18 fl. oz.</p>
    </div>
    <div class="panel back">
      <div class="label">
        <p class="brand">plomvane</p>
        <ul class="claims"><li>No Sulfates</li><li>No Parabens</li><li>No Mineral Oils</li><li>No Artifical Colours</li></ul>
        <p class="directions">Massage into clean dry skin<br>&nbsp;as needed</p>
        <p class="ingredients"><b>Ingredients:</b> Aqua, helianthus annuus seed (sunflower) oil, stearic acid, glycerin, cetearyl alcohol, beeswax, glyceryl stearate, dimethicone, prunus amygdalus dulcis (almond) oil, parfum, phenoxyethanol, triethanolamine, tocopheryl acetate, caprylyl glycol, theobroma cacao seed (cocoa) butter, cocos nucifera (coconut) oil, butyrospermum parki (shea) butter</p>
        <p class="warnings">Discontinue use if irritation occurs.<br>Keep away from children.<br>Avoid Contact with eyes</p>
      </div>
      <div class="icon-row">
        <span class="icon" style="left:2px"></span><span class="icon round" style="left:17px"></span>
        <span class="badge" style="left:57px"></span><span class="badge" style="left:73px"></span><span class="icon round" style="left:90px"></span>
      </div>
      <span class="rule upper" style="left:19px"></span>
      <p class="skin-types">SUITABLE FOR ALL SKIN TYPES</p>
      <span class="rule lower" style="left:19px"></span>
      <p class="address">Unit 5/12 Larkspur Road Brighton VIC 3186</p>
      <p class="contact"><b>plomvane.com.au</b> &nbsp;|&nbsp; sales@plomvane.com.au</p>
    </div>
  </section>

  <section class="variant" style="--c: var(--mauve)">
    <div class="panel front">
      <div class="label">
        <p class="brand">plomvane</p>
        <div class="amp" role="img" aria-label="Faint script ampersand flourish"></div>
        <h2 class="scent long">Fig<br>Sandalwood</h2>
        <p class="tagline">A nourishing,<br>non-greasy<br>hand cream<br>to keep skin<br>soft &amp; hydrated</p>
      </div>
      <p class="script-title">hand cream</p>
      <p class="origin">MADE IN AUSTRALIA</p>
      <p class="volume">35 mL ℮ 1.18 fl. oz.</p>
    </div>
    <div class="panel back">
      <div class="label">
        <p class="brand">plomvane</p>
        <ul class="claims"><li>No Sulfates</li><li>No Parabens</li><li>No Mineral Oils</li><li>No Artifical Colours</li></ul>
        <p class="directions">Massage into clean dry skin<br>&nbsp;as needed</p>
        <p class="ingredients"><b>Ingredients:</b> Aqua, helianthus annuus seed (sunflower) oil, stearic acid, glycerin, cetearyl alcohol, beeswax, glyceryl stearate, dimethicone, prunus amygdalus dulcis (almond) oil, parfum, phenoxyethanol, triethanolamine, tocopheryl acetate, caprylyl glycol, theobroma cacao seed (cocoa) butter, cocos nucifera (coconut) oil, butyrospermum parki (shea) butter</p>
        <p class="warnings">Discontinue use if irritation occurs.<br>Keep away from children.<br>Avoid Contact with eyes</p>
      </div>
      <div class="icon-row">
        <span class="icon" style="left:2px"></span><span class="icon round" style="left:17px"></span>
        <span class="badge" style="left:57px"></span><span class="badge" style="left:73px"></span><span class="icon round" style="left:90px"></span>
      </div>
      <span class="rule upper" style="left:19px"></span>
      <p class="skin-types">SUITABLE FOR ALL SKIN TYPES</p>
      <span class="rule lower" style="left:19px"></span>
      <p class="address">Unit 5/12 Larkspur Road Brighton VIC 3186</p>
      <p class="contact"><b>plomvane.com.au</b> &nbsp;|&nbsp; sales@plomvane.com.au</p>
    </div>
  </section>

  <section class="variant" style="--c: var(--navy)">
    <div class="panel front">
      <div class="label">
        <p class="brand">plomvane</p>
        <div class="amp" role="img" aria-label="Faint script ampersand flourish"></div>
        <h2 class="scent long">Fig<br>Sandalwood</h2>
        <p class="tagline">A nourishing,<br>non-greasy<br>hand cream<br>to keep skin<br>soft &amp; hydrated</p>
      </div>
      <p class="script-title">hand cream</p>
      <p class="origin">MADE IN AUSTRALIA</p>
      <p class="volume">35 mL ℮ 1.18 fl. oz.</p>
    </div>
    <div class="panel back">
      <div class="label">
        <p class="brand">plomvane</p>
        <ul class="claims"><li>No Sulfates</li><li>No Parabens</li><li>No Mineral Oils</li><li>No Artifical Colours</li></ul>
        <p class="directions">Massage into clean dry skin<br>&nbsp;as needed</p>
        <p class="ingredients"><b>Ingredients:</b> Aqua, helianthus annuus seed (sunflower) oil, stearic acid, glycerin, cetearyl alcohol, beeswax, glyceryl stearate, dimethicone, prunus amygdalus dulcis (almond) oil, parfum, phenoxyethanol, triethanolamine, tocopheryl acetate, caprylyl glycol, theobroma cacao seed (cocoa) butter, cocos nucifera (coconut) oil, butyrospermum parki (shea) butter</p>
        <p class="warnings">Discontinue use if irritation occurs.<br>Keep away from children.<br>Avoid Contact with eyes</p>
      </div>
      <div class="icon-row">
        <span class="icon" style="left:2px"></span><span class="icon round" style="left:17px"></span>
        <span class="badge" style="left:57px"></span><span class="badge" style="left:73px"></span><span class="icon round" style="left:90px"></span>
      </div>
      <span class="rule upper" style="left:19px"></span>
      <p class="skin-types">SUITABLE FOR ALL SKIN TYPES</p>
      <span class="rule lower" style="left:19px"></span>
      <p class="address">Unit 5/12 Larkspur Road Brighton VIC 3186</p>
      <p class="contact"><b>plomvane.com.au</b> &nbsp;|&nbsp; sales@plomvane.com.au</p>
    </div>
  </section>
</div>

</body>
</html>
```